Contemporary Elegant Business Card Design for an International Trade Company in the Wine Industry

We need a new business card design for an international trade company in the wine and winemaking industry. The overall feel of the card should be contemporary, upscale, luxurious and elegant. It should communicate confidence and professionalism. The colors should complementary to our logo design (burgundy, gold, and black).
Inspiration: rich velvet tapestry
The card should include the following information:
Business: Corvelle Trading/Shipping, LLC.
Name: Martin R. Obrastow
Title: CEO
Email: marty@corvelletrading.example
Phone: 555-482-1957
www.corvelletrading.example
Reason: We'd like the designers that we requested some additional designs from to still submit designs. Thank you!
Business
Contact Information for Business Card
Title: CEO
Phone: 555-482-1957
www.corvelletrading.example

```html
<!DOCTYPE html>
<html lang="en">
<head>
<meta charset="utf-8">
<title>Corvelle Trading/Shipping – Business Card</title>
<link rel="stylesheet" href="https://fonts.googleapis.com/css2?family=Cinzel:wght@700&family=Lato:wght@400&display=swap">
<style>
  :root {
    --backdrop: #0d0d0d;
    --paper: #ffffff;
    --burgundy: #6f121c;
    --burgundy-mid: #7a1f22;
    --gold: #b87532;
    --copper: #a65a2a;
    --ink: #111111;
    --title-gold: #e0a33c;
    --brand-brown: #8a3a1f;
    --brand-gold: #9c5a28;
  }
  * { margin: 0; padding: 0; box-sizing: border-box; }
  html, body { width: 900px; height: 1200px; overflow: hidden; }
  body {
    background: radial-gradient(ellipse at center, #1b1b1b 0%, var(--backdrop) 75%);
    position: relative;
    font-family: "Lato", Arial, sans-serif;
  }
  .card {
    position: absolute;
    left: 122px;
    width: 654px;
    box-shadow: 0 6px 18px rgba(0,0,0,.6);
    overflow: hidden;
  }
  .card--front { top: 179px; height: 383px; }
  .card--back { top: 629px; height: 382px; }
  .card svg { position: absolute; inset: 0; }

  /* front */
  .brand-name {
    position: absolute; left: 60px; top: 170px; width: 243px;
    font-family: "Cinzel", Georgia, serif;
    font-weight: 700;
    font-size: 32px;
    letter-spacing: 1px;
    color: var(--burgundy);
    text-align: center;
    line-height: 1;
  }
  .contact { position: absolute; left: 384px; top: 128px; color: #fff; }
  .contact__name { font-size: 20px; letter-spacing: .2px; }
  .contact__title { font-size: 15px; color: var(--title-gold); margin-top: 2px; }
  .contact__list { list-style: none; margin-top: 9px; font-size: 15px; }
  .contact__list li { display: flex; align-items: center; gap: 6px; height: 22.5px; }
  .contact__list svg { position: static; width: 15px; height: 13px; }

  /* back */
  .map-field {
    position: absolute; left: 0; top: 0; width: 654px; height: 338px;
    background: radial-gradient(ellipse at 55% 45%, #e4e4e4 0%, #ebebeb 55%, #f6f6f6 100%);
  }
  .brand-mark {
    position: absolute; left: 0; right: 0; top: 122px;
    text-align: center;
    font-family: "Cinzel", Georgia, serif;
  }
  .brand-mark__name {
    font-size: 58px; font-weight: 700; letter-spacing: 3px;
    color: var(--brand-brown); line-height: 1;
  }
  .brand-mark__tag {
    font-size: 24px; font-weight: 700; letter-spacing: .5px;
    color: var(--brand-gold); margin-top: 10px; line-height: 1;
  }
  .back-url {
    position: absolute; left: 0; right: 0; top: 349px;
    text-align: center; color: #fff; font-size: 18px;
  }
</style>
</head>
<body>

<section class="card card--front" aria-label="Business card front">
  <svg width="654" height="383" viewBox="0 0 654 383" aria-hidden="true">
    <defs>
      <linearGradient id="panelFade" x1="0" x2="1" y1="0" y2="0">
        <stop offset="0" stop-color="var(--burgundy)"/>
        <stop offset="0.55" stop-color="var(--burgundy-mid)"/>
        <stop offset="1" stop-color="var(--gold)"/>
      </linearGradient>
      <linearGradient id="tabFade" x1="1" x2="0" y1="0" y2="0">
        <stop offset="0" stop-color="var(--burgundy)"/>
        <stop offset="1" stop-color="var(--copper)"/>
      </linearGradient>
    </defs>
    <rect width="654" height="383" fill="var(--paper)"/>
    <polygon points="327,0 654,0 654,383 327,383 327,303 354,276 354,107 327,82" fill="url(#panelFade)"/>
    <polygon points="0,82 28,107 28,278 0,303" fill="url(#tabFade)"/>
  </svg>

  <div class="brand-name">CORVELLE</div>

  <div class="contact">
    <div class="contact__name">Martin R. Obrastow</div>
    <div class="contact__title">CEO</div>
    <ul class="contact__list">
      <li>
        <svg viewBox="0 0 15 13" aria-hidden="true"><path d="M1 4 Q7.5 -1 14 4 L12 6 L10 4.5 L5 4.5 L3 6 Z M3 7 L12 7 L13 12 L2 12 Z" fill="#fff"/><circle cx="7.5" cy="9.5" r="1.6" fill="#7a1f22"/></svg>
        555-482-1957
      </li>
      <li>
        <svg viewBox="0 0 15 13" aria-hidden="true"><rect x="1" y="2" width="13" height="9" fill="#fff"/><path d="M1 2 L7.5 7.5 L14 2" fill="none" stroke="#7a1f22" stroke-width="1.2"/></svg>
        marty@corvelletrading.example
      </li>
      <li>
        <svg viewBox="0 0 15 13" aria-hidden="true"><rect x="1.5" y="1" width="12" height="8" fill="none" stroke="#fff" stroke-width="1.4"/><rect x="5" y="10.5" width="5" height="1.5" fill="#fff"/></svg>
        www.corvelletrading.example
      </li>
    </ul>
  </div>
</section>

<section class="card card--back" aria-label="Business card back">
  <svg width="654" height="382" viewBox="0 0 654 382" aria-hidden="true">
    <rect width="654" height="382" fill="var(--paper)"/>
  </svg>
  <div class="map-field" role="img" aria-label="Faint grey world map background"></div>
  <svg width="654" height="382" viewBox="0 0 654 382" aria-hidden="true">
    <defs>
      <linearGradient id="bandFade" x1="0" x2="0" y1="0" y2="1">
        <stop offset="0" stop-color="var(--copper)"/>
        <stop offset="1" stop-color="var(--burgundy)"/>
      </linearGradient>
      <linearGradient id="capFade" x1="0" x2="0" y1="0" y2="1">
        <stop offset="0" stop-color="#7c2420"/>
        <stop offset="1" stop-color="#9c4a25"/>
      </linearGradient>
    </defs>
    <polygon points="183,0 470,0 438,33 215,33" fill="url(#capFade)"/>
    <polygon points="0,308 183,308 215,338 438,338 470,308 654,308 654,382 0,382" fill="url(#bandFade)"/>
  </svg>
  <div class="brand-mark">
    <div class="brand-mark__name">CORVELLE</div>
    <div class="brand-mark__tag">TRADING/SHIPPING, LLC</div>
  </div>
  <div class="back-url">www.corvelletrading.example</div>
</section>

</body>
</html>
```